wealth management firm, professional group, new model

we have a logo that works but we need a card, white background using our colors...clean look

our tag line if can be used in

The Bridge From Client to Owner

```html
<!DOCTYPE html>
<html lang="en">
<head>
<meta charset="utf-8">
<title>Arcel Wealth Partners – Business Card</title>
<link rel="stylesheet" href="https://fonts.googleapis.com/css2?family=Lato:wght@300;400&family=Montserrat:wght@300;400&display=swap">
<style>
  :root {
    --navy: #172d4f;
    --white: #ffffff;
    --page: #ffffff;
    --edge: #d9dde3;
  }
  * { margin: 0; padding: 0; box-sizing: border-box; }
  html, body {
    width: 1200px;
    height: 1200px;
    overflow: hidden;
    background: var(--page);
  }
  .canvas {
    position: relative;
    width: 1200px;
    height: 1200px;
  }
  .card {
    position: absolute;
    left: 171px;
    width: 857px;
    height: 501px;
  }
  .card--back {
    top: 74px;
    background: var(--navy);
    color: var(--white);
  }
  .card--front {
    top: 623px;
    background: var(--white);
    color: var(--navy);
    border: 1px solid var(--edge);
  }

  /* Back side */
  .back-name {
    position: absolute;
    top: 112px;
    left: 0;
    width: 100%;
    text-align: center;
    font-family: "Montserrat", sans-serif;
    font-weight: 300;
    font-size: 54px;
    letter-spacing: 0.42em;
    text-indent: 0.42em;
    color: var(--white);
  }
  .contact-list {
    position: absolute;
    top: 334px;
    left: 158px;
    list-style: none;
    font-family: "Lato", sans-serif;
    font-weight: 300;
    font-size: 21px;
  }
  .contact-list li {
    display: flex;
    align-items: center;
    height: 39.5px;
  }
  .contact-icon {
    width: 16px;
    height: 16px;
    margin-right: 14px;
    fill: var(--white);
    flex: none;
  }
  .address {
    position: absolute;
    top: 351px;
    left: 444px;
    width: 251px;
    border-top: 1.5px solid var(--white);
    padding-top: 32px;
    display: flex;
    align-items: flex-start;
    font-family: "Lato", sans-serif;
    font-weight: 300;
    font-size: 21px;
    line-height: 29px;
    font-style: normal;
  }
  .address .contact-icon {
    margin-top: 6px;
    margin-right: 16px;
  }

  /* Front side */
  .front-name {
    position: absolute;
    top: 222px;
    left: 0;
    width: 100%;
    text-align: center;
    font-family: "Montserrat", sans-serif;
    font-weight: 300;
    font-size: 82px;
    line-height: 1;
    letter-spacing: 0.5em;
    text-indent: 0.5em;
  }
  .front-descriptor {
    position: absolute;
    top: 346px;
    left: 0;
    width: 100%;
    text-align: center;
    font-family: "Montserrat", sans-serif;
    font-weight: 400;
    font-size: 29px;
    letter-spacing: 0.14em;
    text-indent: 0.14em;
  }
</style>
</head>
<body>
<main class="canvas">

  <section class="card card--back" aria-label="Card back">
    <div class="back-name">ARCEL</div>

    <ul class="contact-list">
      <li>
        <svg class="contact-icon" viewBox="0 0 16 16" aria-hidden="true">
          <path d="M8 1a7 7 0 1 0 0 14A7 7 0 0 0 8 1zm0 1.5c.6.7 1.1 1.9 1.3 3.3H6.7C6.9 4.4 7.4 3.2 8 2.5zM5.2 5.8H3a5.5 5.5 0 0 1 3-3c-.4.8-.7 1.8-.8 3zm0 1.5c0 .5 0 1 .1 1.5H2.6a5.6 5.6 0 0 1 0-1.5h2.6zm1.5 0h2.6a9 9 0 0 1 0 1.5H6.7a9 9 0 0 1 0-1.5zm4.1 0h2.6a5.6 5.6 0 0 1 0 1.5h-2.7l.1-1.5zm-.1-1.5c-.1-1.2-.4-2.2-.8-3a5.5 5.5 0 0 1 3 3h-2.2zM3 10.3h2.2c.1 1.2.4 2.2.8 3a5.5 5.5 0 0 1-3-3zm3.7 0h2.6c-.2 1.4-.7 2.6-1.3 3.3-.6-.7-1.1-1.9-1.3-3.3zm4.1 0H13a5.5 5.5 0 0 1-3 3c.4-.8.7-1.8.8-3z"/>
        </svg>
        <span>Arcelwealth.net</span>
      </li>
      <li>
        <svg class="contact-icon" viewBox="0 0 16 16" aria-hidden="true">
          <path d="M3.6 1.5l2.1-.3 1.2 3-1.4 1.1a8.6 8.6 0 0 0 4.2 4.2l1.1-1.4 3 1.2-.3 2.1c-.1.6-.7 1.1-1.3 1.1C6.6 12.5 2.5 8.4 2.5 2.8c0-.6.5-1.2 1.1-1.3z"/>
        </svg>
        <span>620-555-0148</span>
      </li>
      <li>
        <svg class="contact-icon" viewBox="0 0 16 16" aria-hidden="true">
          <path d="M2 3h12a1 1 0 0 1 1 1v8a1 1 0 0 1-1 1H2a1 1 0 0 1-1-1V4a1 1 0 0 1 1-1zm0 1.6V5l6 3.8L14 5v-.4L8 8.3 2 4.6z"/>
        </svg>
        <span>info@arcelwealth.net</span>
      </li>
    </ul>

    <address class="address">
      <svg class="contact-icon" viewBox="0 0 16 16" aria-hidden="true">
        <path d="M8 1a4.8 4.8 0 0 0-4.8 4.8C3.2 9.4 8 15 8 15s4.8-5.6 4.8-9.2A4.8 4.8 0 0 0 8 1zm0 6.6a1.8 1.8 0 1 1 0-3.6 1.8 1.8 0 0 1 0 3.6z"/>
      </svg>
      <span>48 W 9th Ave, Ste 210<br>Marlow, KS 60014</span>
    </address>
  </section>

  <section class="card card--front" aria-label="Card front">
    <div class="front-name">ARCEL</div>
    <div class="front-descriptor">WEALTH PARTNERS</div>
  </section>

</main>
</body>
</html>
```